Business Card and Letterhead for Juniper Anvil - (Have Logo)

Update 4: Removed company reg no from business card details as it looked a bit out of place. Updated services list.
UPDATE 3
Sorry, I got the address a little bit wrong, have updated it below. Sorry for any inconvenience caused.
UPDATE 2
Finally I have the details for the business cards and letterhead. Submissions already made do not have to be updated unless shortlisted, if all new submissions could include the details for me, Marcus, that would be very much appreciated and help with the final shortlist selection. I intend to share a shortlist of the three best entries with past and existing customers for their feedback and opinions. Thank you all again for your time.
Here are the details.
Marcus Telby
Web Developer
T: 01632 960 418
E: marcus@juniperanvil.example
www.juniperanvil.example
Professional Photography
Web Solutions & E-Commerce
Audio & HD Video Production
Marketing & Promotions
Identity and Branding
Juniper Anvil Ltd
Suite 20938, 3rd Floor
212-224 Orchard Lane
London, N7 9QX
Company Reg. No: 05829147
The order and the layout of the information are of course down to the design, but the company registration number should be smaller and less prominent. The formatting of the telephone and email address using a T: and an E: I am not sure about and again if it is Tel: or Email: or Icons is up to the design.
The Company No. on the letterhead should read (somewhere in small text along the bottom):
Juniper Anvil is a Ltd Company registered in England & Wales, Registration No. 05829147.
The second business card details are
Oliver Brackley
Photographer
T: 01632 960 418
E: oliver@juniperanvil.example
Everything else the same of course.
Thank you again for all the submissions so far.
END OF UPDATE 2
-
UPDATE 1: Please do not alter the logo nor the logo colours. (This was a previous pixel forum project and I am extremely happy with it. The icon can stand alone of course, but I have had to eliminate all entries that have made it black and white, or reversed the icon.) I would like to thank everyone that has participated so far and am very grateful for all your thought and time.
End of Update 1
-
Original Brief:
I have attached the logo vector file.
Following a superb logo from a previous Pixel Forum project I am now looking for a business card design and (although less important) a letterhead as well.
I must admit I tried to do it myself but could only come up with the usual amateur stuff that in comparison to the quality of the logo looked awful.
About Us
Juniper Anvil Ltd will be a new company due to start in January. It is really just me (a web developer) and my friend (a photographer). We will be aiming at the usual small to medium sized businesses in the local area, selling various digital services including photographic services to the public, web hosting and development, commercial photography, modelling services (not us!), full video and film production and possibly a bit of marketing as well. (Really it is anything we can do professionally all lumped together! We met running seperate businesses which have both since closed)
We will not be competing on price. We plan to be expensive but fair. Certainly not the cheapest.
What we are looking for
Business Card
I imagine a double sided business card, which will be used for more than one person. I imagine the front to be the same for everyone and the persons details to be on the back, although this is of course only my thoughts and I am of course completely open to any ideas.
The card could also have a services list or a bit about what we do on it. It might feature the website address, our business address (mail forwarding address) or our registered company number.
Or it might have none of that, we are completely open to any ideas and have no real fixed opinions. I just want it to be really nice :-)
Letterhead (secondary importance)
We will make our decision primarily on the business card, although a mathcing letterhead would be fantastic. Something standardish in format and simple, although again, all ideas are welcomed.
I hope that is enough information but if you have any questions I will answer them as fully and as quickly as possible.
Thank you once again and I really look forward to seeing your ideas and picking a winner.
Marcus T.
Small businesses AND the general public
Film Production

```html
<!DOCTYPE html>
<html lang="en">
<head>
<meta charset="utf-8">
<title>Juniper Anvil – Letterhead and Business Cards</title>
<link rel="stylesheet" href="https://fonts.googleapis.com/css2?family=Arimo:wght@400;700&family=Tinos:wght@400;700&display=swap">
<style>
  :root {
    --stage: #b3b3b3;
    --paper: #ffffff;
    --edge: #1a1a1a;
    --brand-red: #b5121b;
    --brand-red-light: #e04a50;
    --brand-ink: #3d3d3d;
    --text: #111111;
    --faint-mark: #f5dcdd;
  }
  * { box-sizing: border-box; margin: 0; padding: 0; }
  html, body { width: 1200px; height: 991px; overflow: hidden; }
  body {
    background: var(--stage);
    position: relative;
    font-family: "Tinos", "Times New Roman", serif;
    color: var(--text);
  }
  .stage-rule {
    position: absolute; left: 0; width: 1200px; height: 1px; background: #555;
  }
  .stage-rule--top { top: 1px; }
  .stage-rule--bottom { top: 988px; }

  .sheet {
    position: absolute;
    background: var(--paper);
    border: 1px solid var(--edge);
    overflow: hidden;
  }
  .corner { position: absolute; }
  .corner svg { display: block; }

  /* Letterhead */
  .letterhead { left: 86px; top: 229px; width: 476px; height: 609px; }
  .letterhead .corner--top { left: 0; top: 0; }
  .letterhead .corner--bottom { right: 0; bottom: 0; }
  .wordmark {
    position: absolute;
    display: flex; align-items: center; gap: 8px;
    font-family: "Arimo", Arial, sans-serif;
    font-weight: 700;
    color: var(--brand-ink);
    letter-spacing: 1px;
    white-space: nowrap;
  }
  .wordmark__square { background: var(--brand-red); flex: none; }
  .letterhead .wordmark { left: 106px; top: 50px; font-size: 34px; }
  .letterhead .wordmark__square { width: 40px; height: 40px; }
  .faint-mark {
    position: absolute; left: 150px; top: 251px;
    width: 187px; height: 187px; background: var(--faint-mark);
  }
  .letterhead__address {
    position: absolute; left: 12px; top: 497px;
    font-size: 12px; line-height: 14.4px;
  }

  /* Contact card */
  .card { width: 322px; height: 182px; }
  .card--contact { left: 815px; top: 232px; }
  .card .corner--top { left: 0; top: 0; }
  .card .corner--bottom { right: 0; bottom: 0; }
  .card__person {
    position: absolute; left: 30px; top: 52px; width: 94px;
    text-align: center; font-weight: 700; font-size: 12.5px; line-height: 13.5px;
  }
  .card__details {
    position: absolute; left: 136px; top: 52px;
    font-size: 12px; line-height: 13.3px;
  }

  /* Services card */
  .card--services { left: 687px; top: 446px; width: 324px; }
  .card--services .wordmark { left: 78px; top: 20px; font-size: 24px; }
  .card--services .wordmark__square { width: 28px; height: 28px; }
  .services {
    position: absolute; left: 0; top: 89px; width: 100%;
    text-align: center; font-family: "Arimo", Arial, sans-serif;
    font-size: 12px; line-height: 14.2px;
  }
  .services__title { font-weight: 700; font-size: 13px; line-height: 15px; }
  .services ul { list-style: none; }
  .card__web {
    position: absolute; left: 5px; top: 165px; font-size: 12px;
  }
</style>
</head>
<body>
  <div class="stage-rule stage-rule--top"></div>

  <section class="sheet letterhead" aria-label="Letterhead">
    <div class="corner corner--top">
      <svg width="215" height="170" viewBox="0 0 215 170" role="img" aria-label="Red fine-line pattern sweeping across the top-left corner">
        <defs>
          <linearGradient id="lh-top" x1="0" y1="0" x2="1" y2="1">
            <stop offset="0" stop-color="var(--brand-red)"/>
            <stop offset="1" stop-color="var(--brand-red-light)"/>
          </linearGradient>
        </defs>
        <path d="M0 0 H210 C110 12 25 70 10 165 L0 168 Z" fill="url(#lh-top)"/>
      </svg>
    </div>
    <div class="wordmark"><span class="wordmark__square"></span>JUNIPER ANVIL</div>
    <div class="faint-mark" aria-hidden="true"></div>
    <address class="letterhead__address" style="font-style:normal">
      Juniper Anvil<br>
      4810 E. Larkspur<br>
      Ridgeford,Ca. 90021<br>
      Ph: 555-014-0737<br>
      Fax: 555-014-0738<br>
      Email: juniperanvil@mail.example<br>
      Web: www.juniperanvil.example
    </address>
    <div class="corner corner--bottom">
      <svg width="212" height="160" viewBox="0 0 212 160" role="img" aria-label="Red fine-line pattern sweeping across the bottom-right corner">
        <defs>
          <linearGradient id="lh-bottom" x1="1" y1="1" x2="0" y2="0">
            <stop offset="0" stop-color="var(--brand-red)"/>
            <stop offset="1" stop-color="var(--brand-red-light)"/>
          </linearGradient>
        </defs>
        <path d="M212 0 C196 90 120 145 0 160 H212 Z" fill="url(#lh-bottom)"/>
      </svg>
    </div>
  </section>

  <section class="sheet card card--contact" aria-label="Business card, contact side">
    <div class="corner corner--top">
      <svg width="84" height="84" viewBox="0 0 84 84" role="img" aria-label="Red fine-line pattern in the top-left corner">
        <defs>
          <linearGradient id="bc-top" x1="0" y1="0" x2="1" y2="1">
            <stop offset="0" stop-color="var(--brand-red)"/>
            <stop offset="1" stop-color="var(--brand-red-light)"/>
          </linearGradient>
        </defs>
        <path d="M0 0 H82 C40 8 12 38 4 82 L0 84 Z" fill="url(#bc-top)"/>
      </svg>
    </div>
    <div class="card__person">Dale Morrow<br>C.E.O</div>
    <div class="card__details">
      4810 E. Larkspur<br>
      Ridgeford,Ca. 90021<br>
      Ph: 555-014-0847<br>
      Fax: 555-014-0738<br>
      Email: dale.morrow@mail.example
    </div>
    <div class="corner corner--bottom">
      <svg width="152" height="88" viewBox="0 0 152 88" role="img" aria-label="Red fine-line pattern in the bottom-right corner">
        <defs>
          <linearGradient id="bc-bottom" x1="1" y1="1" x2="0" y2="0">
            <stop offset="0" stop-color="var(--brand-red)"/>
            <stop offset="1" stop-color="var(--brand-red-light)"/>
          </linearGradient>
        </defs>
        <path d="M152 0 C140 50 90 80 0 88 H152 Z" fill="url(#bc-bottom)"/>
      </svg>
    </div>
  </section>

  <section class="sheet card card--services" aria-label="Business card, services side">
    <div class="corner corner--top">
      <svg width="95" height="80" viewBox="0 0 95 80" role="img" aria-label="Red fine-line pattern in the top-left corner">
        <defs>
          <linearGradient id="sc-top" x1="0" y1="0" x2="1" y2="1">
            <stop offset="0" stop-color="var(--brand-red)"/>
            <stop offset="1" stop-color="var(--brand-red-light)"/>
          </linearGradient>
        </defs>
        <path d="M0 0 H93 C45 8 12 38 4 78 L0 80 Z" fill="url(#sc-top)"/>
      </svg>
    </div>
    <div class="wordmark"><span class="wordmark__square"></span>JUNIPER ANVIL</div>
    <div class="services">
      <p class="services__title">Areas of expertise backed by quality service:</p>
      <ul>
        <li>Web Hosting and developement</li>
        <li>Full video and Film Production</li>
        <li>Photography</li>
        <li>Modeling Services</li>
      </ul>
    </div>
    <div class="card__web">www.juniperanvil.example</div>
    <div class="corner corner--bottom">
      <svg width="116" height="104" viewBox="0 0 116 104" role="img" aria-label="Red fine-line pattern in the bottom-right corner">
        <defs>
          <linearGradient id="sc-bottom" x1="1" y1="1" x2="0" y2="0">
            <stop offset="0" stop-color="var(--brand-red)"/>
            <stop offset="1" stop-color="var(--brand-red-light)"/>
          </linearGradient>
        </defs>
        <path d="M116 0 C108 60 70 95 0 104 H116 Z" fill="url(#sc-bottom)"/>
      </svg>
    </div>
  </section>

  <div class="stage-rule stage-rule--bottom"></div>
</body>
</html>
```